Quotecraft services

I provide collision estimating for autobody shops, so when they need a collision estimate and they are too busy or don't have the software, i write that estimate for them. I do this either in person or virtual. I need a postcard mailer design, 6.25 x 9 inches, with a header that reads QUOTECRAFT SERVICES, highlighting 20+ years of experience, and text that reads ASK ABOUT OUR TRAINING

Target Market(s)

Autobody Repair shops

Industry/Entity Type

Autobody

```html
<!DOCTYPE html>
<html lang="en">
<head>
<meta charset="UTF-8">
<title>Quotecraft Services Mailer</title>
<link href="https://fonts.googleapis.com/css2?family=Open+Sans:wght@400;700&display=swap" rel="stylesheet">
<style>
  :root{
    --stage:#0f2f3b;
    --ink:#050505;
    --white:#ffffff;
    --flame:#ff4a0d;
    --photo-dark:#3a3f44;
    --photo-mid:#8a6a4e;
    --photo-orange:#e8761c;
  }
  html,body{margin:0;padding:0;width:1200px;height:1000px;overflow:hidden;background:var(--stage);}
  .mailer{
    position:absolute;left:323px;top:110px;width:554px;height:780px;
    background:var(--ink);font-family:"Open Sans",Arial,sans-serif;color:var(--white);
    box-shadow:0 10px 30px rgba(0,0,0,.45);
  }
  .mailer__art{position:absolute;left:0;top:0;width:554px;height:780px;}
  .mailer__header{
    position:absolute;top:30px;left:0;width:554px;padding-left:30px;box-sizing:border-box;
    text-align:center;font-weight:700;font-size:36px;letter-spacing:.5px;margin:0;
  }
  .brand{
    position:absolute;top:500px;left:0;width:554px;text-align:center;
    font-weight:700;font-size:26px;letter-spacing:2px;color:var(--flame);
  }
  .experience{
    position:absolute;top:578px;left:0;width:554px;text-align:center;
    font-size:23px;margin:0;
  }
  .cta-lead{
    position:absolute;top:624px;left:0;width:554px;text-align:center;
    font-size:27px;color:var(--flame);margin:0;letter-spacing:.5px;
  }
  .cta-main{
    position:absolute;top:658px;left:0;width:554px;text-align:center;
    font-weight:700;font-size:60px;margin:0;letter-spacing:1px;
  }
</style>
</head>
<body>
  <div class="mailer">
    <svg class="mailer__art" viewBox="0 0 554 780" xmlns="http://www.w3.org/2000/svg">
      <defs>
        <linearGradient id="photoTone" x1="0" y1="0" x2="1" y2="0.3">
          <stop offset="0" stop-color="var(--photo-dark)"/>
          <stop offset="0.35" stop-color="var(--photo-orange)"/>
          <stop offset="0.75" stop-color="var(--photo-orange)"/>
          <stop offset="1" stop-color="var(--photo-mid)"/>
        </linearGradient>
      </defs>
      <line class="header-rule" x1="110" y1="88" x2="460" y2="88" stroke="var(--flame)" stroke-width="3"/>
      <path class="hero-photo" role="img" aria-label="Photo of an orange sports coupe in a body shop, seen from the rear three-quarter view"
            d="M0 168 Q300 158 554 122 L554 385 Q330 478 0 362 Z" fill="url(#photoTone)"/>
      <path class="band band--white" d="M0 140 Q300 130 554 98" fill="none" stroke="var(--white)" stroke-width="7"/>
      <path class="band band--flame" d="M0 158 Q300 148 554 114" fill="none" stroke="var(--flame)" stroke-width="14"/>
      <path class="band band--flame" d="M0 368 Q330 482 554 392" fill="none" stroke="var(--flame)" stroke-width="12"/>
      <path class="band band--white" d="M0 384 Q330 500 554 406" fill="none" stroke="var(--white)" stroke-width="6"/>
      <line class="footer-rule" x1="170" y1="742" x2="390" y2="742" stroke="var(--flame)" stroke-width="3"/>
    </svg>
    <h1 class="mailer__header">QUOTECRAFT SERVICES</h1>
    <div class="brand">PANELWISE</div>
    <p class="experience">20 + years of experience</p>
    <p class="cta-lead">ASK ABOUT OUR</p>
    <p class="cta-main">TRAINING</p>
  </div>
</body>
</html>
```